Poster to advertise new mind coaching clinic

Create a single sided A4 colour poster using the text provided. Suggested image provided. You may want to suggest an alternative however images need to appeal to both male and female sports people.

Text:
One-to-one mind coaching
For recreational and competitive sports people
Learn the mental tools and techniques used by the top sports people to fulfil your potential

 Create well-formed and achievable goals
 Overcome limiting beliefs
 Accelerate mastery through modelling your heroes
 Learn how to use mental rehearsal to increase your chances of success
 Smash through belief ceilings
 Get into the zone to bring your ‘A-Game’ more often
Thursdays in central Twyford
5-8pm
For more information contact:
thebluekitecoaching@postmere.com
Tel: 07481 265314
www.the-blue-kite.co.uk

Target Market(s)

sports people

Industry/Entity Type

Clinic

Requirements
Must have
• All the content provided. Contact details.

```html
<!DOCTYPE html>
<html lang="en">
<head>
<meta charset="utf-8">
<title>One-to-One Mind Coaching – The Blue Kite</title>
<link rel="stylesheet" href="https://fonts.googleapis.com/css2?family=Montserrat:wght@700;800&family=Tenor+Sans&family=Roboto+Condensed:wght@400&display=swap">
<style>
  :root {
    --track-blue: #2f7fc4;
    --track-deep: #1d5c9a;
    --band-red: #c24a55;
    --panel-blue: #29bdec;
    --ink: #111111;
    --alert-red: #e3141c;
    --tagline-yellow: #f4f0a0;
    --white: #ffffff;
    --footer: #111111;
  }
  * { margin: 0; padding: 0; box-sizing: border-box; }
  html, body { width: 848px; height: 1200px; overflow: hidden; background: var(--white); }
  .poster { position: relative; width: 848px; height: 1200px; overflow: hidden; font-family: "Tenor Sans", sans-serif; }

  .hero-photo {
    position: absolute; left: 0; top: 0; width: 848px; height: 674px;
    background: radial-gradient(ellipse at 50% 45%, #8a5a46 0%, #6a4a48 16%, rgba(47,127,196,0) 34%),
                linear-gradient(180deg, var(--track-blue) 0%, #3a8bd0 50%, var(--track-deep) 100%);
  }
  .tagline {
    position: absolute; top: 10px; left: 0; width: 848px; text-align: center;
    color: var(--tagline-yellow); font-size: 27px; line-height: 40px; letter-spacing: 0.3px;
  }
  .title-band {
    position: absolute; left: 0; top: 520px; width: 848px; height: 94px;
    background: var(--band-red); text-align: center; color: var(--white);
  }
  .title-band h1 {
    font-family: "Montserrat", sans-serif; font-weight: 800; font-size: 45px;
    line-height: 50px; padding-top: 6px; letter-spacing: 0.2px;
  }
  .title-band p { font-size: 28px; line-height: 32px; }

  .benefits {
    position: absolute; left: 0; top: 674px; width: 474px; height: 476px;
    background: var(--panel-blue); padding: 26px 0 0 44px; list-style: none;
  }
  .benefits li {
    position: relative; padding-left: 35px; font-size: 23.5px; line-height: 38.5px; color: var(--ink);
  }
  .benefits li svg { position: absolute; left: 0; top: 10px; width: 26px; height: 24px; }

  .details {
    position: absolute; left: 474px; top: 674px; width: 374px; height: 476px;
    background: var(--white); text-align: center;
  }
  .schedule {
    font-family: "Roboto Condensed", sans-serif; color: var(--alert-red);
    font-size: 37px; line-height: 49px; margin-top: 37px; letter-spacing: -0.8px;
  }
  .hours { font-family: "Roboto Condensed", sans-serif; color: var(--alert-red); font-size: 25px; letter-spacing: -0.8px; line-height: 30px; }
  .brand {
    display: flex; align-items: center; justify-content: center; gap: 14px;
    height: 140px; margin-top: 14px;
  }
  .brand-dot { width: 26px; height: 26px; border-radius: 50%; background: var(--panel-blue); }
  .brand-name { font-size: 38px; color: var(--ink); }
  .contact { color: var(--alert-red); font-size: 20px; line-height: 31px; margin-top: 22px; }
  .contact .email { font-size: 17.5px; }

  .site-footer {
    position: absolute; left: 0; top: 1150px; width: 848px; height: 50px;
    background: var(--footer); color: var(--white); text-align: center;
    font-size: 27px; line-height: 50px; letter-spacing: 0.5px;
  }
</style>
</head>
<body>
<div class="poster">
  <div class="hero-photo" role="img" aria-label="Photo of a sprinter crossing the finish line on a blue indoor track with arms raised in celebration"></div>
  <p class="tagline">Learn the mental tools and techniques used<br>by the top sports people to fulfil your potential</p>

  <header class="title-band">
    <h1>ONE-TO-ONE MIND COACHING</h1>
    <p>For recreational and competitive sports people</p>
  </header>

  <ul class="benefits">
    <li><svg viewBox="0 0 26 24"><path d="M2 13 L9 21 L24 2" fill="none" stroke="#e3141c" stroke-width="4" stroke-linecap="round" stroke-linejoin="round"/></svg>Create well-formed and<br>achievable goals</li>
    <li><svg viewBox="0 0 26 24"><path d="M2 13 L9 21 L24 2" fill="none" stroke="#e3141c" stroke-width="4" stroke-linecap="round" stroke-linejoin="round"/></svg>Overcome limiting beliefs</li>
    <li><svg viewBox="0 0 26 24"><path d="M2 13 L9 21 L24 2" fill="none" stroke="#e3141c" stroke-width="4" stroke-linecap="round" stroke-linejoin="round"/></svg>Accelerate mastery through<br>modelling your heroes</li>
    <li><svg viewBox="0 0 26 24"><path d="M2 13 L9 21 L24 2" fill="none" stroke="#e3141c" stroke-width="4" stroke-linecap="round" stroke-linejoin="round"/></svg>Learn how to use mental<br>rehearsal to increase your<br>chances of success</li>
    <li><svg viewBox="0 0 26 24"><path d="M2 13 L9 21 L24 2" fill="none" stroke="#e3141c" stroke-width="4" stroke-linecap="round" stroke-linejoin="round"/></svg>Smash through belief ceilings</li>
    <li><svg viewBox="0 0 26 24"><path d="M2 13 L9 21 L24 2" fill="none" stroke="#e3141c" stroke-width="4" stroke-linecap="round" stroke-linejoin="round"/></svg>Get into the zone to bring your<br>‘A-Game’ more often.</li>
  </ul>

  <section class="details">
    <p class="schedule">THURSDAYS IN<br>CENTRAL TWYFORD</p>
    <p class="hours">5-8pm</p>
    <div class="brand">
      <span class="brand-dot"></span>
      <span class="brand-name">The Blue Kite</span>
    </div>
    <p class="contact">For more information contact:<br><span class="email">thebluekitecoaching@postmere.com</span><br>Tel: 07481 265314</p>
  </section>

  <footer class="site-footer">www.the-blue-kite.co.uk</footer>
</div>
</body>
</html>
```